Corporate Brightfen business cards to be handed to investor, bankers etc. Needs to have a young feel

I need business cards designed for a technology company that provides uber-like rapid response on the security industry. I would like it simple but very cool and tasteful. See attached documents for artwork and colours to be used. Cut sheet describes business model. Card stock should be thicker than normal. I would like the one side to be just the art and the other to have the contact info with maybe the pin somewhere.

Target Market(s)

Investors

Industry/Entity Type

Business

Contact Information for Business Card

Would like the logo attached on one side with name address and other info on the other side.

Font styles to use
Other font styles liked:
• See existing logo

Colors
6b449b
886aae
e4daeb
ffffff

Requirements
Must have
• Name: Dorian Felkatsis
• Address: 47 Larkfield Avenue, Toronto, On, M6K2B7
• Tel: 416-7291846
• Email: rolo@brightfen.io
Nice to have
• See logo colours

```html
<!DOCTYPE html>
<html lang="en">
<head>
<meta charset="utf-8">
<title>Brightfen Business Card</title>
<link rel="stylesheet" href="https://fonts.googleapis.com/css2?family=Questrial&display=swap">
<style>
  :root {
    --purple-deep: #6b449b;
    --purple-mid: #886aae;
    --purple-soft: #7d5cad;
    --lilac: #e4daeb;
    --white: #ffffff;
    --ink: #1d1a22;
    --backdrop: #2b2b2d;
  }
  * { margin: 0; padding: 0; box-sizing: border-box; }
  html, body { width: 1200px; height: 880px; overflow: hidden; background: var(--backdrop); }
  .stage {
    width: 1200px; height: 880px;
    display: flex; flex-direction: column; align-items: center; justify-content: center; gap: 40px;
  }
  .card {
    position: relative; width: 700px; height: 400px; border-radius: 24px; overflow: hidden;
    box-shadow: 0 14px 34px rgba(0,0,0,0.45);
  }

  /* Front side */
  .card-front { background: var(--purple-deep); }
  .front-art { position: absolute; inset: 0; }
  .brand-name {
    position: absolute; left: 0; right: 0; top: 160px;
    text-align: center;
    font-family: "Questrial", sans-serif; font-weight: 400; font-size: 72px;
    color: var(--white); line-height: 1; letter-spacing: 1px;
  }

  /* Back side */
  .card-back { background: var(--white); }
  .identity {
    position: absolute; left: 0; right: 0; top: 0; height: 230px;
    display: flex; flex-direction: column; align-items: center; justify-content: center; gap: 18px;
  }
  .avatar { width: 90px; height: 90px; border-radius: 50%; background: var(--lilac); }
  .holder-name {
    font-family: "Questrial", sans-serif; font-weight: 400; font-size: 42px;
    color: var(--ink); letter-spacing: 1px;
  }
  .contact-band {
    position: absolute; left: 0; right: 0; bottom: 0; height: 170px;
    display: grid; grid-template-columns: 1fr 1fr 1fr;
  }
  .contact-cell {
    display: flex; flex-direction: column; align-items: center; justify-content: flex-start;
    padding-top: 20px; gap: 16px; text-align: center;
  }
  .contact-cell.deep { background: var(--purple-deep); }
  .contact-cell.mid { background: var(--purple-mid); }
  .contact-icon {
    width: 78px; height: 78px; border-radius: 50%; background: var(--lilac);
    display: flex; align-items: center; justify-content: center;
  }
  .contact-text {
    font-family: "Questrial", sans-serif; font-size: 17px; line-height: 1.35;
    color: var(--white); letter-spacing: 0.5px;
  }
</style>
</head>
<body>
<main class="stage">

  <section class="card card-front" aria-label="Card front">
    <svg class="front-art" width="700" height="400" viewBox="0 0 700 400" aria-hidden="true">
      <circle cx="520" cy="110" r="470" fill="var(--purple-soft)"/>
      <circle cx="270" cy="170" r="118" fill="var(--purple-deep)"/>
    </svg>
    <p class="brand-name">Brightfen</p>
  </section>

  <section class="card card-back" aria-label="Card back">
    <div class="identity">
      <div class="avatar" role="img" aria-label="Person avatar icon"></div>
      <h1 class="holder-name">Dorian Felkatsis</h1>
    </div>
    <div class="contact-band">
      <div class="contact-cell deep">
        <div class="contact-icon">
          <svg width="44" height="32" viewBox="0 0 44 32" aria-hidden="true">
            <rect x="1" y="1" width="42" height="30" rx="2" fill="var(--white)" stroke="var(--purple-mid)" stroke-width="2"/>
            <path d="M2 2 L22 18 L42 2" fill="none" stroke="var(--purple-mid)" stroke-width="2"/>
          </svg>
        </div>
        <p class="contact-text">rolo@brightfen.io</p>
      </div>
      <div class="contact-cell mid">
        <div class="contact-icon">
          <svg width="32" height="42" viewBox="0 0 32 42" aria-hidden="true">
            <path d="M16 41 C16 41 2 24 2 15 A14 14 0 0 1 30 15 C30 24 16 41 16 41 Z" fill="var(--white)" stroke="var(--purple-mid)" stroke-width="2"/>
            <circle cx="16" cy="15" r="5" fill="var(--purple-mid)"/>
          </svg>
        </div>
        <p class="contact-text">47 Larkfield Avenue<br>Toronto, On, M6K2B7</p>
      </div>
      <div class="contact-cell deep">
        <div class="contact-icon">
          <svg width="26" height="44" viewBox="0 0 26 44" aria-hidden="true">
            <rect x="1" y="1" width="24" height="42" rx="4" fill="var(--white)" stroke="var(--purple-mid)" stroke-width="2"/>
            <rect x="5" y="6" width="16" height="28" fill="var(--lilac)"/>
            <circle cx="13" cy="38.5" r="2" fill="var(--purple-mid)"/>
          </svg>
        </div>
        <p class="contact-text">416-7291846</p>
      </div>
    </div>
  </section>

</main>
</body>
</html>
```